BRIMclean - Towel Wash Package/Label Design

Design a label and look for a towel wash under the brand BRIMclean.

To be printed on either a Standup Zipper Pouch, and/or outer box.

Product Features:
Removes and Prevents Musty Odours
Increase & Restore Absorbency
Remove Buildup from Hard Water, Softeners and Detergents

Sample concept as starting point attached.

Target Market(s)

Women ages 25-55

Industry/Entity Type

Product

Font styles to use
Sans Serif
Script

Requirements
Must have
• Clean look
• Good use of one or two colours
• Imply Freshness, and Quality
• Easily identify what the products is used for.
Nice to have
• The feeling like a brand that already existed...
• Warm and welcoming colours
Should not have
• To many colour or overcomplicated deisgn

```html
<!DOCTYPE html>
<html lang="en">
<head>
<meta charset="utf-8">
<title>BRIMclean Towel &amp; Laundry Freshener Label</title>
<link rel="stylesheet" href="https://fonts.googleapis.com/css2?family=Fredoka:wght@600&family=Nunito:wght@600;700&display=swap">
<style>
  :root {
    --green: #4cb83a;
    --green-dark: #2f9a2a;
    --navy: #1e3f73;
    --sky-top: #c9ecfb;
    --sky-bottom: #8fd6f3;
    --white: #ffffff;
    --ink: #1a1a1a;
  }
  * { margin: 0; padding: 0; box-sizing: border-box; }
  html, body { width: 791px; height: 1200px; overflow: hidden; background: var(--white); }
  .canvas { position: relative; width: 791px; height: 1200px; }

  .brand-mark {
    position: absolute; left: 0; right: 0; top: 60px;
    display: flex; justify-content: center; align-items: center; gap: 14px;
  }
  .brand-dot { width: 30px; height: 30px; border-radius: 50%; background: var(--green); }
  .brand-name {
    font-family: "Fredoka", sans-serif; font-weight: 600;
    font-size: 64px; color: var(--green); letter-spacing: 1px;
  }

  .label {
    position: absolute; left: 185px; top: 300px; width: 421px; height: 610px;
    background: var(--white); overflow: hidden; border-radius: 2px;
  }
  .label-brand {
    height: 170px; display: flex; justify-content: center; align-items: center; gap: 10px;
  }
  .label-brand .brand-dot { width: 22px; height: 22px; }
  .label-brand .brand-name { font-size: 50px; }

  .label-panel {
    position: absolute; left: 0; right: 0; top: 170px; height: 290px;
    background: linear-gradient(180deg, var(--sky-top), var(--sky-bottom));
  }
  .product-title {
    position: absolute; left: 0; right: 0; top: 28px; text-align: center;
    font-family: "Nunito", sans-serif; font-weight: 700;
    font-size: 40px; line-height: 1.12; color: var(--navy);
  }
  .usage-icon {
    position: absolute; left: 50%; top: 172px; width: 78px; height: 78px;
    margin-left: -39px;
  }
  .wave { position: absolute; left: 0; top: 400px; width: 421px; height: 80px; }

  .feature-list {
    position: absolute; left: 0; right: 0; top: 476px; text-align: center; list-style: none;
    font-family: "Nunito", sans-serif; font-weight: 700;
    font-size: 13px; line-height: 1.3; color: var(--green-dark);
  }
  .net-weight {
    position: absolute; left: 0; right: 0; top: 566px; text-align: center;
    font-family: "Nunito", sans-serif; font-weight: 700; font-size: 17px; line-height: 1.2; color: var(--ink);
  }
</style>
</head>
<body>
<main class="canvas">
  <header class="brand-mark">
    <span class="brand-dot"></span>
    <span class="brand-name">BRIMclean</span>
  </header>

  <section class="label">
    <div class="label-brand">
      <span class="brand-dot"></span>
      <span class="brand-name">BRIMclean</span>
    </div>

    <div class="label-panel">
      <h1 class="product-title">Towel &amp;<br>Laundry<br>Freshener</h1>
      <svg class="usage-icon" viewBox="0 0 78 78" aria-label="Towel icon">
        <circle cx="39" cy="39" r="37" fill="var(--green)"/>
        <circle cx="39" cy="39" r="31" fill="none" stroke="var(--white)" stroke-width="2"/>
        <line x1="20" y1="24" x2="58" y2="24" stroke="var(--white)" stroke-width="3" stroke-linecap="round"/>
        <rect x="25" y="24" width="28" height="30" fill="none" stroke="var(--white)" stroke-width="3" stroke-linejoin="round"/>
        <line x1="25" y1="46" x2="53" y2="46" stroke="var(--white)" stroke-width="2"/>
      </svg>
    </div>

    <svg class="wave" viewBox="0 0 421 80" preserveAspectRatio="none" aria-hidden="true">
      <path d="M0 30 C120 70 260 0 421 22 L421 80 L0 80 Z" fill="var(--white)"/>
      <path d="M0 26 C120 66 260 -4 421 18" fill="none" stroke="var(--green)" stroke-width="6"/>
      <path d="M0 40 C130 74 270 12 421 32" fill="none" stroke="var(--green)" stroke-width="2.5" opacity="0.7"/>
    </svg>

    <ul class="feature-list">
      <li>Removes and Prevents Musty Odours</li>
      <li>Increase &amp; Restore Absorbency</li>
      <li>Remove Buildup from Hard Water,</li>
      <li>Softeners and Detergents</li>
    </ul>
    <p class="net-weight">500G</p>
  </section>
</main>
</body>
</html>
```